London's best branded & leading residential inventory company requires sales pack design

Good Afternoon,

We are looking for design and print company to start working with. We have a couple of initial projects and will definitely have other projects in the future that we would require help with.

Below I have outlined the current projects that we need help with.

Amber Otter – www.amber-otter-demo.co.uk

SALES PACKS – We have our business development manager out in the field who is visiting current and new clients. We want to stand out and be different so are open to suggestions and ways of presenting ourselves and being front of mind. Our ideas about what we want are below, we do not want the pack to be heavy with tonnes of information.

We want to create one for the professional marketing leading brand we have. We would like the pack to be small and inter changeable.

Below are the values of the company which need to be communicated through USP’s/quotes as well as the design of the pack itself.
AO VALUES
• Professional
• Solution Driven
• Trusted Partner
• Consistent
• Progressive
• Personable
RB VALUES
• Quality
• Trusted Partner
• Solution Driven
• Progressive
• Energetic
• Personable

Below is the layout we would like to give you some clear guidance as to what to produce.

Design an A5 folder – landscape, which has the 3 cards in. Below is exactly the content required and the

Every card and side should have Amber Otter logo and strap line, Tel – 020 7946 0318 Email – bookings@amber-otter-demo.co.uk, QRSM & NEVB Accreditation

CARD 1 – Front (use branding any photos use subtly)
CUSTOMER FOCUS
- Open 7 days a week – 364 Days a year
- Inspections from 8am to 8pm
- 50 clerks during peak periods
- Dedicated bookings managers for every client

CARD 2 - Front (use branding any photos use subtly)
REPORT GUARANTEE & QUALITY
- 100% guarantee all reports back within 48 hours
- Reports created accurately and consistently using bespoke app ‘TrueLog’
- 19 point quality check from proof readers for every report
- All clerks receive monthly site inspection from Head of Training

CARD 3 – Front (use branding any photos use subtly)
WHY AMBER OTTER – Use photo Soren Pelby with below quote
“At Amber Otter we are dedicated to service, with the office support team open 7 days a week we can guarantee detailed management of the inspections 364 days a year (we do close for xmas!). Let us provide you with a great service by calling or emailing our team of dedicated Booking Managers for any needs or requirements”
The have the following bullet points below
- Over 45,000 inspections Carried out to the highest professional standards
- Trusted partner to 145 agents, including the most respected estate agents in London
- We know the value of a home, so we donate 5% of our profits in support of Harbourway - the UK's leading charity for homeless young people. (also have their logo in same colour as text - see front page of one of our reports that we have also now uploaded)

CARD 1 – BACK - TESTIMONIALS – Use the photos, logo and quotes.
Dunmores
Pemberly Stoke

CARD 2 – BACK - TESTIMONIALS – Use the photos, logo and quotes.
Tilby & Crowe
Ormand Fitch

CARD 3 – BACK - BACK - TESTIMONIALS – Use the photos, logo and quotes.
Peter R Hale
Fernleys

FRONT COVER OF FOLDER
AMBER OTTER – THE PROFESSIONAL INVENTORY COMPANY – (Use Logo & Strap line)

BACK COVER
FLYING HIGH ABOVE THE REST (The strap line)

INSIDE FRONT COVER – Use photo image of AO in the field

INSIDE BACK COVER – Use photo image of AO in the field (this section we must be able to slot the 3 cards)

CARD 4 NEW ADDITION
This needs to be a card can be perforated and divided into 4 (as per business cards), this idea being this card will be split and handed round to various people in our clients offices
So front of each card will have photo of bookings manager (use Soren Pelby for now), their name and role, must have our logo and strap line and contact details, with the words 'YOUR DEDICATED BOOKINGS MANAGER'
The BACK of each section (4 sections as to back of business card) to have our selling points, as per our reports front cover (see new upload) - must have logo and contact details as well (phone no and email)
- Open 7 days a week, 364 days a year
- Office open from 8.45am to 6.30pm
- Guaranteed 48 hour return of reports
- Over 45,000 inspections completed
- Up to 50 clerks in peak times

Target Market(s)

Estate Agents

Industry/Entity Type

It Company

Font styles to use
Other font styles liked:
• Those outlined in Brand Principles

Requirements
Nice to have
• Photos of Bookings Managers themselves - only Soren Pelby on website is current

```html
<!DOCTYPE html>
<html lang="en">
<head>
<meta charset="utf-8">
<title>Amber Otter – Sales Cards</title>
<link href="https://fonts.googleapis.com/css2?family=Roboto+Condensed:wght@300;400;700&display=swap" rel="stylesheet">
<style>
  :root {
    --navy: #1f2b4d;
    --green: #1fae4b;
    --band: #e4e4e4;
    --paper: #ffffff;
    --edge: #dcdcdc;
    --ink: #2a2a2a;
    --muted: #6b6b6b;
    --badge: #b9bec6;
  }
  * { margin: 0; padding: 0; box-sizing: border-box; }
  html, body { width: 1200px; height: 394px; overflow: hidden; background: var(--paper); }
  .sheet { position: relative; width: 1200px; height: 394px; }
  .card {
    position: absolute; top: 0; width: 571px; height: 394px;
    background: var(--paper); border: 1px solid var(--edge); overflow: hidden;
  }
  .card--customer { left: 0; }
  .card--quality { left: 629px; }
  .card__band { position: absolute; left: 0; top: 70px; width: 100%; height: 252px; background: var(--band); }
  .card__lines { position: absolute; inset: 0; pointer-events: none; }

  .brand { position: absolute; top: 18px; left: 0; width: 100%; text-align: center; }
  .brand__name {
    font-family: 'Roboto Condensed', sans-serif; font-weight: 700;
    font-size: 25px; letter-spacing: 0.6px; color: var(--navy); line-height: 1;
  }
  .brand__tagline {
    margin-top: 4px; font-family: 'Roboto Condensed', sans-serif; font-weight: 400;
    font-size: 5.5px; letter-spacing: 0.9px; color: var(--green);
  }

  .card__title {
    position: absolute; top: 77px; left: 0; width: 100%; text-align: center;
    font-family: 'Roboto Condensed', sans-serif; font-weight: 700;
    font-size: 13px; line-height: 16px; color: var(--navy);
  }

  .points {
    position: absolute; list-style: none;
    font-family: 'Roboto Condensed', sans-serif; font-weight: 300;
    font-size: 13px; line-height: 15px; color: var(--ink);
  }
  .points li::before { content: "\00B7"; font-weight: 700; margin-right: 5px; }
  .card--customer .points { left: 24px; top: 98px; width: 215px; }
  .card--customer .points li { margin-bottom: 14.5px; }
  .card--quality .points { left: 181px; top: 98px; width: 206px; }
  .card--quality .points li { margin-bottom: 14px; }

  .photo { position: absolute; overflow: hidden; }
  .photo::after {
    content: ""; position: absolute; right: 0; top: 0; width: 0; height: 0;
    border-top: 14px solid var(--green); border-left: 14px solid transparent;
  }
  .photo--keys { left: 245px; top: 98px; width: 145px; height: 211px; background: linear-gradient(160deg, #c9c9c9, #8d8d8d 60%, #b5a99a); }
  .photo--kitchen { left: 401px; top: 98px; width: 145px; height: 99px; background: linear-gradient(180deg, #6e6e6e, #b9b9b7 55%, #4a4a4a); }
  .photo--bedroom { left: 401px; top: 210px; width: 145px; height: 99px; background: linear-gradient(120deg, #d7cdbf, #8a7b6a 55%, #efefef); }
  .photo--clerk { left: 25px; top: 98px; width: 144px; height: 211px; background: linear-gradient(100deg, #d9cfc0, #a08a6e 40%, #3a3232 75%, #e6e1da); }
  .photo--hob { left: 402px; top: 98px; width: 144px; height: 99px; background: linear-gradient(160deg, #3b3b3b, #8b6a45 45%, #d9d9d6); }
  .photo--tablet { left: 402px; top: 210px; width: 144px; height: 99px; background: linear-gradient(180deg, #a9b3b3, #eef0f0 50%, #5a5a55); }

  .footer { position: absolute; left: 0; top: 350px; width: 100%; height: 30px; }
  .badges { position: absolute; left: 54px; top: 10px; display: flex; gap: 8px; align-items: center; }
  .badge { background: var(--badge); }
  .badge--square { width: 36px; height: 17px; border-radius: 2px; }
  .badge--round { width: 17px; height: 17px; border-radius: 50%; }
  .contact {
    position: absolute; left: 202px; top: 11px; display: flex; gap: 10px;
    font-family: 'Roboto Condensed', sans-serif; font-weight: 400;
    font-size: 4.6px; line-height: 6px; color: var(--muted);
  }
  .contact__key { margin-right: 3px; }
  .contact__row { display: flex; }
</style>
</head>
<body>
<main class="sheet">

  <section class="card card--customer">
    <div class="card__band"></div>
    <svg class="card__lines" width="571" height="394" viewBox="0 0 571 394" aria-hidden="true">
      <polyline points="102,0 68,34 36,34 0,72" fill="none" stroke="#1fae4b" stroke-width="0.8"/>
      <polyline points="571,292 536,326 504,326 468,394" fill="none" stroke="#1fae4b" stroke-width="0.8"/>
    </svg>

    <header class="brand">
      <div class="brand__name">AMBER OTTER</div>
      <div class="brand__tagline">THE PROFESSIONAL INVENTORY COMPANY</div>
    </header>

    <h2 class="card__title">CUSTOMER FOCUS</h2>
    <ul class="points">
      <li>Open 7 days a week – 364 Days a year</li>
      <li>Inspections from 8am to 8pm</li>
      <li>50 clerks during peak periods</li>
      <li>Dedicated bookings managers for every client</li>
    </ul>

    <div class="photo photo--keys" role="img" aria-label="Photo of a set of house keys being handed over"></div>
    <div class="photo photo--kitchen" role="img" aria-label="Photo of a clerk with a tablet in a modern kitchen"></div>
    <div class="photo photo--bedroom" role="img" aria-label="Photo of a clerk checking a bedside lamp with a tablet"></div>

    <footer class="footer">
      <div class="badges">
        <span class="badge badge--square"></span>
        <span class="badge badge--round"></span>
        <span class="badge badge--square"></span>
      </div>
      <div class="contact">
        <div><span class="contact__key">A |</span>Amber Otter Property Services Ltd<br>4th Floor Marlow House,<br>Elder Park, Croydon, CR0 9ZZ</div>
        <div>
          <div class="contact__row"><span class="contact__key">T |</span>+44 (0)20 7946 0318</div>
          <div class="contact__row"><span class="contact__key">E |</span>bookings@amber-otter-demo.co.uk</div>
          <div class="contact__row"><span class="contact__key">W |</span>amber-otter-demo.co.uk</div>
        </div>
      </div>
    </footer>
  </section>

  <section class="card card--quality">
    <div class="card__band"></div>
    <svg class="card__lines" width="571" height="394" viewBox="0 0 571 394" aria-hidden="true">
      <polyline points="102,0 68,34 36,34 0,72" fill="none" stroke="#1fae4b" stroke-width="0.8"/>
      <polyline points="571,292 536,326 504,326 468,394" fill="none" stroke="#1fae4b" stroke-width="0.8"/>
    </svg>

    <header class="brand">
      <div class="brand__name">AMBER OTTER</div>
      <div class="brand__tagline">THE PROFESSIONAL INVENTORY COMPANY</div>
    </header>

    <h2 class="card__title">REPORT GUARANTEE &amp; QUALITY</h2>
    <ul class="points">
      <li>100% guarantee all reports back within 48 hours</li>
      <li>Reports created accurately and consistently using bespoke app ‘TrueLog’</li>
      <li>19 point quality check from proof readers for every report</li>
      <li>All clerks receive monthly site inspection from Head of Training</li>
    </ul>

    <div class="photo photo--clerk" role="img" aria-label="Photo of a clerk inspecting a lamp while holding a tablet"></div>
    <div class="photo photo--hob" role="img" aria-label="Photo of a kitchen hob with a wooden bowl"></div>
    <div class="photo photo--tablet" role="img" aria-label="Photo of a clerk recording a kitchen on a tablet"></div>

    <footer class="footer">
      <div class="badges">
        <span class="badge badge--square"></span>
        <span class="badge badge--round"></span>
        <span class="badge badge--square"></span>
      </div>
      <div class="contact">
        <div><span class="contact__key">A |</span>Amber Otter Property Services Ltd<br>4th Floor Marlow House,<br>Elder Park, Croydon, CR0 9ZZ</div>
        <div>
          <div class="contact__row"><span class="contact__key">T |</span>+44 (0)20 7946 0318</div>
          <div class="contact__row"><span class="contact__key">E |</span>bookings@amber-otter-demo.co.uk</div>
          <div class="contact__row"><span class="contact__key">W |</span>amber-otter-demo.co.uk</div>
        </div>
      </div>
    </footer>
  </section>

</main>
</body>
</html>
```